WeatheredIt.net wordpress design

Concept: Website where personal stories, personal videos can be posted as a challenge while awaiting the wisdom of experience from others who have WeatheredIt.net same event or challenge in their lifetime.
Support aspects will be in 4 quadrants of Challenges:
1. Financial 2. Medical & Physical
3. Legal Matters 4. Psychological & Spiritual - ability to chat online with a spiritual/psychological counselor or life coach
Updates
Wanted to thank all of you for your designs! Greatly appreciated. Very creative ideas that captured the essence of this website. Will be back with a selection very shortly.
Target Market(s)
Anyone looking for a solution based upon experiential wisdom
Industry/Entity Type
Financial
Requirements
Must have
- Interactive website: Where you can post a challenge or issue via a written question or a video and ask for a solution.
Ability to access any of the 4 Quadrants (as listed above) to ask for an expert, via experience, advice and wisdom from those who have similar challenges.

```html
<!DOCTYPE html>
<html lang="en">
<head>
<meta charset="utf-8">
<title>WeatheredIt.net</title>
<link href="https://fonts.googleapis.com/css2?family=Alfa+Slab+One&family=Arimo:wght@400;700&family=Lora:ital,wght@0,700;1,400;1,700&display=swap" rel="stylesheet">
<style>
:root{
  --orange:#fdb94a;
  --orange-dark:#f5a623;
  --red:#f05a33;
  --link-red:#e05a2b;
  --dark:#333333;
  --header-bg:#f7f7f7;
  --hero-bg:#e4ddd9;
  --card-bg:#f3f3f3;
  --panel-bg:#efeee8;
  --text:#333;
  --white:#fff;
}
*{margin:0;padding:0;box-sizing:border-box}
html,body{width:1120px;height:1200px;overflow:hidden;background:#fff;font-family:"Arimo",Arial,sans-serif;color:var(--text)}
.abs{position:absolute}
.slab{font-family:"Alfa Slab One",Georgia,serif;font-weight:400}
.site-header{left:0;top:0;width:1120px;height:98px;background:var(--header-bg)}
.logo{left:183px;top:6px;width:197px;height:84px;display:flex;align-items:center;gap:8px}
.logo-mark{width:22px;height:22px;background:var(--orange-dark)}
.logo-name{font-family:"Arimo",sans-serif;font-weight:700;font-size:21px;color:var(--orange-dark)}
.btn{height:27px;border-radius:2px;font-size:11.5px;display:flex;align-items:center;justify-content:center}
.btn-register{left:730px;top:14px;width:98px;background:linear-gradient(#ffd15c,#f7ae21);border:1px solid #e8a21c}
.btn-signin{left:835px;top:14px;width:99px;background:linear-gradient(#eee,#d4d4d4);border:1px solid #bbb}
.search{left:465px;top:56px;width:469px;height:31px;display:flex;border:1px solid #ccc}
.search-field{flex:1;background:#fff;font-family:"Lora",serif;font-style:italic;font-size:12px;color:#666;padding:0 13px;display:flex;align-items:center}
.search-btn{width:100px;background:var(--dark);color:#fff;font-size:11.5px;display:flex;align-items:center;justify-content:center}
.topic-banner{left:183px;top:106px;width:752px;height:36px;background:var(--orange);font-size:18.5px;padding-left:18px;display:flex;align-items:center;color:#222}
.tabs{left:183px;top:142px;width:752px;height:47px;background:var(--dark);display:flex}
.tab{color:#fff;font-weight:700;font-size:13.5px;display:flex;align-items:center}
.tab.active{background:var(--orange);color:#222;width:107px;justify-content:center}
.hero{left:183px;top:189px;width:752px;height:169px;background:var(--hero-bg)}
.hero-photo{position:absolute;right:0;top:0;width:255px;height:169px;background:radial-gradient(circle at 60% 50%,#c97a5e 0%,#b8826c 30%,#d6bfb4 60%,var(--hero-bg) 100%)}
.subnav{position:absolute;left:0;top:12px;height:27px;display:flex;align-items:center;font-size:11.2px;color:#222}
.subnav .current{background:var(--orange);height:27px;width:102px;display:flex;align-items:center;justify-content:center}
.subnav .sep{margin:0 9px}
.subnav small{font-size:8px;font-style:italic;font-weight:700}
.hero-title{position:absolute;left:60px;top:80px;width:486px;text-align:center;font-family:"Lora",serif;font-weight:700;font-size:17px;line-height:20px;color:#111}
.ask-label{left:183px;top:374px;font-size:14.4px;color:#222}
.login-badge{left:324px;top:374px;width:78px;height:19px;background:var(--orange);font-size:9.5px;font-weight:700;display:flex;align-items:center;justify-content:center}
.ask-box{left:185px;top:398px;width:433px;height:87px;background:var(--panel-bg);border:1px solid #ddd}
.ask-submit{left:618px;top:398px;width:91px;height:87px;background:var(--dark);color:var(--orange);font-size:17px;display:flex;align-items:center;justify-content:center}
.coach{left:720px;top:398px;width:214px;height:87px}
.coach-head{height:29px;background:var(--dark);color:#fff;font-weight:700;font-size:13px;display:flex;align-items:center;justify-content:center}
.coach-body{height:58px;background:var(--red);color:#fff;display:flex;align-items:center;padding-left:8px;gap:12px;font-size:14px}
.section-title{font-size:20.5px;color:#111}
.card{top:539px;height:177px;background:var(--card-bg);padding:10px 10px 0}
.card-head{display:flex;gap:7px}
.avatar{width:46px;height:46px;border:2px solid #d8d2c0;background:linear-gradient(#d9b79a,#b98b6c)}
.card-title{font-size:16px;color:#222;margin-top:0}
.card-meta{font-size:9.6px;font-weight:700;margin-top:6px}
.card-body{font-size:10.3px;line-height:12.6px;text-align:justify;margin-top:14px;color:#444}
.card-body p+p{margin-top:5px}
.read-more{text-align:right;font-family:"Lora",serif;font-style:italic;font-weight:700;font-size:11px;color:var(--link-red);margin-top:8px;padding-right:2px}
.testimonial{left:186px;width:480px;font-size:10.3px;line-height:12.8px;color:#333}
.testimonial p+p{margin-top:5px}
.testimonial .who{font-weight:700;font-size:9.6px;margin-top:8px}
.divider{left:686px;top:724px;height:220px;border-left:1px dotted #777}
.questions{left:690px;top:764px;width:244px;height:176px;background:var(--panel-bg);padding:10px 7px;font-size:10.3px;line-height:20px;color:#222}
.footer{left:0;top:976px;width:1120px;height:168px;background:var(--dark)}
.f-col{top:1007px}
.f-col h3{color:var(--orange);font-size:20px;font-family:"Alfa Slab One",serif;font-weight:400}
.f-col ul{list-style:none;margin-top:8px;padding-left:2px}
.f-col li{color:#fff;font-size:10.4px;line-height:17.2px}
.social li{display:flex;align-items:center;gap:12px;line-height:25.6px;font-size:11px;letter-spacing:.3px}
.social i{width:19px;height:19px;background:#5a6f9e;display:block}
.legal{left:0;top:1144px;width:1120px;height:56px;background:var(--orange);text-align:center;font-size:10.4px;line-height:17.6px;padding-top:12px;color:#222}
</style>
</head>
<body>
<header class="abs site-header"></header>
<div class="abs logo"><span class="logo-mark"></span><span class="logo-name">WeatheredIt.net</span></div>
<div class="abs btn btn-register">Register</div>
<div class="abs btn btn-signin">Sign In</div>
<div class="abs search"><div class="search-field">Search Experiences/Challenges</div><div class="search-btn">Search</div></div>

<div class="abs topic-banner slab">Select your topic and get motivated, Sharing Experience, Post concern...</div>
<nav class="abs tabs">
  <div class="tab active">Financial</div>
  <div class="tab" style="margin-left:18px">Medical &amp; Physical</div>
  <div class="tab" style="margin-left:58px">Legal Matters</div>
  <div class="tab" style="margin-left:54px">Psychological &amp; Spiritual</div>
</nav>
<section class="abs hero">
  <div class="hero-photo" role="img" aria-label="Hand holding copper coins"></div>
  <div class="subnav">
    <span class="current">Post Question</span><span class="sep">|</span>Post a Video<span class="sep">|</span>Read Experienceses<span class="sep">|</span>Get Motivated<span class="sep">|</span>View Solutions&nbsp;<small>( Sign In please )</small>
  </div>
  <h1 class="hero-title">Sharing of life's experiences getting through similar challenges to those asking "how to survive”</h1>
</section>

<div class="abs ask-label">Submit your question</div>
<div class="abs login-badge">Please login</div>
<div class="abs ask-box"></div>
<div class="abs ask-submit slab">Submit</div>
<div class="abs coach">
  <div class="coach-head">Chat online with Life Coach</div>
  <div class="coach-body">
    <svg width="56" height="42" viewBox="0 0 56 42"><ellipse cx="35" cy="15" rx="17" ry="13" fill="#fff"/><path d="M44 25l6 9-12-6z" fill="#fff"/><ellipse cx="20" cy="25" rx="17" ry="13" fill="#fff" stroke="#f05a33" stroke-width="3"/><path d="M10 35l-5 7 12-5z" fill="#fff"/></svg>
    <span class="slab">Councelor Online</span>
  </div>
</div>

<h2 class="abs section-title slab" style="left:183px;top:503px">Featured Experiences</h2>
<article class="abs card" style="left:183px;width:247px">
  <div class="card-head"><div class="avatar" role="img" aria-label="Portrait of a smiling boy"></div><div><div class="card-title">How I ran Marathon</div><div class="card-meta">Sam Crane, 19 years, Milan</div></div></div>
  <div class="card-body"><p>Contrary to popular belief, Lorem Ipsum is not simply random text. It has roots in a piece of classical Latin literature from 45 BC, making it over 2000 years old.</p><p>Richard Hallworth, a Latin professor at Hampden-</p></div>
  <div class="read-more">Read more</div>
</article>
<article class="abs card" style="left:442px;width:240px">
  <div class="card-head"><div class="avatar" role="img" aria-label="Portrait of an older man"></div><div><div class="card-title">My Financial Life :|</div><div class="card-meta">Daniel Shore, 70 years, US</div></div></div>
  <div class="card-body"><p>Contrary to popular belief, Lorem Ipsum is not simply random text. It has roots in a piece of classical Latin literature from 45 BC, making it over 2000 years old.</p><p>Richard Hallworth, a Latin professor at Hampden-</p></div>
  <div class="read-more">Read more</div>
</article>
<article class="abs card" style="left:689px;width:245px">
  <div class="card-head"><div class="avatar" role="img" aria-label="Portrait of a smiling woman"></div><div><div class="card-title">I won the Life again :)</div><div class="card-meta">Yummy Momy, 30 years, India</div></div></div>
  <div class="card-body"><p>Contrary to popular belief, Lorem Ipsum is not simply random text. It has roots in a piece of classical Latin literature from 45 BC, making it over 2000 years old.</p><p>Richard Hallworth, a Latin professor at Hampden-</p></div>
  <div class="read-more">Read more</div>
</article>

<h2 class="abs section-title slab" style="left:183px;top:730px">Testimonials</h2>
<div class="abs testimonial" style="top:771px"><p>Contrary to popular belief, Lorem Ipsum is not simply random text. It has roots in a piece of classical Latin literature from 45 BC, making it over 2000 years old.</p><p>Richard Hallworth, a Latin professor at Hampden-</p><p class="who">Sam Crane, 19 years, Milan</p></div>
<div class="abs testimonial" style="top:851px"><p>Contrary to popular belief, Lorem Ipsum is not simply random text. It has roots in a piece of classical Latin literature from 45 BC, making it over 2000 years old.</p><p>Richard Hallworth, a Latin professor at Hampden-</p><p class="who">Sam Crane, 19 years, Milan</p></div>
<div class="abs divider"></div>
<h2 class="abs section-title slab" style="left:690px;top:730px">Recent Questions</h2>
<div class="abs questions">
  <div>- Are U happy or sad with ur life ?</div>
  <div>- When I’ll be a hero of my life?</div>
  <div>- Will my husband return to me again?</div>
  <div>- Is I’m bad?</div>
  <div>- Lorem Ipsum is still dummy text?</div>
  <div>- What is Lorem Ipsum?</div>
  <div>- Will I win next race in my locality?</div>
  <div>- How to post question here?</div>
</div>

<footer class="abs footer"></footer>
<div class="abs f-col" style="left:243px"><h3>About</h3><ul><li>Home</li><li>About WeatheredIt.net</li><li>The Project</li><li>Testimonials</li><li>Contact</li></ul></div>
<div class="abs f-col" style="left:402px"><h3>Help</h3><ul><li>How to Register</li><li>Forgot Account Credentials</li><li>Register Online</li><li>Video Posting</li><li>Send An Email</li></ul></div>
<div class="abs f-col" style="left:578px"><h3>Experience</h3><ul><li>Financial</li><li>Medical &amp; Physical</li><li>Legal Matters</li><li>Psycological Matter</li><li>Spiritual Matter</li></ul></div>
<div class="abs f-col" style="left:754px"><h3>Get Social</h3><ul class="social"><li><i></i>Circlebook</li><li><i style="background:#4aa8d8"></i>Chirper</li><li><i style="background:#555"></i>Plusone</li></ul></div>
<div class="abs legal">Privacy Policy | Terms of Service | Sitemap<br>© WeatheredIt.net, 2012 - 2013. All Rights Reserved. Unauthorized reproduction is strictly forbidden.</div>
</body>
</html>
```